Delmer's Pressure Washing Services

Starting a pressure washing business on my own in Central Valley California, not too much experience so affordable, I do houses, fences, driveways, cars, trailers, RVs. Planning to make this full-time hoping clientele picks up after having a nice business card. Design doesn't have to be flashy, more to the point, I like simplistic/personable. I do not want something exhausting to look at or with too much going on.

Target Market(s)

Residential, Commercial

Industry/Entity Type

Pressure Washing

Contact Information for Business Card

avalible Services

Font styles to use
Sans Serif

Colors
0054AA
0677BA
7BADD7
CADEEF
E8F1F8
0094D4
00A9DD
6FCCEA
C7EBF8
E9F6FB
00AB8E
00BBA5
67D7C9
C6EFE9
E9F9F6

```html
<!DOCTYPE html>
<html lang="en">
<head>
<meta charset="utf-8">
<title>Delmer's Pressure Washing Services – Business Card</title>
<link href="https://fonts.googleapis.com/css2?family=Bebas+Neue&family=Oswald:wght@300;400&display=swap" rel="stylesheet">
<style>
  :root {
    --backdrop: #cfcfcf;
    --card-light: #e9e9ea;
    --card-dark: #262626;
    --card-dark-edge: #1c1c1c;
    --ink: #1a1a1a;
    --wave-light: #dcdcdd;
    --wave-mid: #cdcdce;
    --paper: #f2f2f2;
    --rule: #9a9a9a;
  }
  html, body {
    margin: 0;
    padding: 0;
    width: 1200px;
    height: 1101px;
    overflow: hidden;
    background: var(--backdrop);
  }
  .canvas {
    position: relative;
    width: 1200px;
    height: 1101px;
  }
  .card {
    position: absolute;
    top: 266px;
    width: 302px;
    height: 533px;
    overflow: hidden;
  }
  .card--front {
    left: 246px;
    background: var(--card-light);
    color: var(--ink);
  }
  .card--back {
    left: 641px;
    color: var(--paper);
  }
  .wave-band {
    position: absolute;
    inset: 0;
    background: linear-gradient(200deg, var(--wave-mid) 0%, var(--wave-light) 100%);
    clip-path: polygon(302px 60px, 302px 150px, 250px 182px, 200px 212px, 150px 240px, 100px 265px, 50px 288px, 0 310px, 0 238px, 50px 228px, 100px 212px, 150px 190px, 200px 160px, 250px 118px);
  }
  .owner-name {
    position: absolute;
    left: 34px;
    top: 56px;
    margin: 0;
    font-family: "Bebas Neue", sans-serif;
    font-weight: 400;
    font-size: 43px;
    line-height: 52px;
    letter-spacing: 1.5px;
  }
  .contact {
    position: absolute;
    left: 34px;
    margin: 0;
    font-family: "Bebas Neue", sans-serif;
    font-size: 25px;
    line-height: 31px;
    letter-spacing: 0.5px;
  }
  .contact--reach { top: 351px; }
  .contact--area { top: 428px; }
  .social-name {
    position: absolute;
    right: 22px;
    top: 457px;
    margin: 0;
    font-family: "Bebas Neue", sans-serif;
    font-size: 19px;
    line-height: 20px;
    letter-spacing: 0.5px;
  }
  .surface-texture {
    position: absolute;
    inset: 0;
    background: radial-gradient(ellipse at 45% 40%, #333 0%, var(--card-dark) 55%, var(--card-dark-edge) 100%);
  }
  .brand {
    position: absolute;
    left: 0;
    right: 0;
    top: 160px;
    text-align: center;
  }
  .brand__name {
    margin: 0;
    font-family: "Bebas Neue", sans-serif;
    font-weight: 400;
    font-size: 59px;
    line-height: 62px;
    letter-spacing: 3.5px;
  }
  .brand__rule {
    width: 219px;
    height: 1px;
    margin: 4px auto 0;
    background: var(--rule);
  }
  .brand__tagline {
    margin: 8px 0 0;
    font-family: "Bebas Neue", sans-serif;
    font-size: 24px;
    line-height: 24px;
    letter-spacing: 0.3px;
  }
  .services {
    position: absolute;
    left: 0;
    right: 0;
    top: 426px;
    margin: 0;
    text-align: center;
    font-family: "Oswald", sans-serif;
    font-weight: 300;
    font-size: 16px;
    line-height: 30px;
    letter-spacing: 0.3px;
    text-transform: uppercase;
  }
  .services__sep { padding: 0 6px; color: var(--paper); }
</style>
</head>
<body>
<main class="canvas">
  <section class="card card--front" aria-label="Card front">
    <div class="wave-band" role="img" aria-label="Faint grey flowing line pattern"></div>
    <h1 class="owner-name">Delmer<br>Ruiz</h1>
    <p class="contact contact--reach">209 555 0142<br>EMAIL@ADDRESS.COM</p>
    <p class="contact contact--area">Central Valley<br>California</p>
    <p class="social-name">DelmerPW</p>
  </section>

  <section class="card card--back" aria-label="Card back">
    <div class="surface-texture" role="img" aria-label="Dark cracked asphalt surface texture"></div>
    <div class="brand">
      <h2 class="brand__name">DELMER'S</h2>
      <div class="brand__rule"></div>
      <p class="brand__tagline">Pressure Washing Services</p>
    </div>
    <p class="services">
      Houses<span class="services__sep">|</span>Fences<span class="services__sep">|</span>Driveways<br>
      Cars<span class="services__sep">|</span>Trailers<span class="services__sep">|</span>RVs
    </p>
  </section>
</main>
</body>
</html>
```